continuing medical education travel company. luxury, professional, quality service

PLEASE USE THE REVISED LOGO FOR ALL CARD DESIGNS, NO SNAKE HEAD

Target Market(s)

physicians

Industry/Entity Type

Travel Industry

Contact Information for Business Card

luxury quality, spot uv, foil, rounded corners

Colors
0255a3
3176b5
cfdeed
aaaaaa
5c5c5c

Requirements
Must have
• navy, platinum, possible holographic

```html
<!DOCTYPE html>
<html lang="en">
<head>
<meta charset="utf-8">
<title>Velora Travel – Business Card</title>
<link href="https://fonts.googleapis.com/css2?family=Arimo:wght@400;700&display=swap" rel="stylesheet">
<style>
  :root {
    --navy: #2c2d8f;
    --platinum-dark: #8e8e8e;
    --platinum-light: #a9a9a9;
    --ring-grey: #aaaaaa;
    --white: #ffffff;
    --backdrop: #e9e9ec;
  }
  * { box-sizing: border-box; margin: 0; padding: 0; }
  html, body {
    width: 1200px; height: 950px; overflow: hidden;
    background: var(--backdrop);
    font-family: "Arimo", Arial, sans-serif;
  }
  .canvas { position: relative; width: 1200px; height: 950px; }

  .card {
    position: absolute;
    width: 560px; height: 320px;
    border-radius: 24px;
    overflow: hidden;
    box-shadow: 0 10px 28px rgba(0,0,0,0.18);
  }

  /* Back of card */
  .card-back {
    left: 60px; top: 120px;
    background: linear-gradient(160deg, var(--platinum-light), var(--platinum-dark));
    color: var(--white);
    display: flex; flex-direction: column; align-items: center; justify-content: center;
  }
  .brand-name {
    font-weight: 400;
    text-align: center;
    line-height: 1;
  }
  .card-back .brand-name { color: var(--white); }
  .brand-name .word-main { display: block; font-size: 58px; letter-spacing: 4px; }
  .brand-name .word-sub { display: block; font-size: 22px; letter-spacing: 18px; margin-top: 8px; padding-left: 18px; }
  .card-back .web { margin-top: 26px; font-size: 13px; letter-spacing: 3px; }

  /* Front of card */
  .card-front { left: 580px; top: 500px; background: var(--navy); }
  .card-front .shape { position: absolute; inset: 0; }
  .card-front .brand-name {
    position: absolute; left: 300px; top: 82px; width: 230px;
    color: var(--navy);
  }
  .card-front .brand-name .word-main { font-size: 44px; letter-spacing: 3px; }
  .card-front .brand-name .word-sub { font-size: 17px; letter-spacing: 13px; padding-left: 13px; margin-top: 6px; }

  .person { position: absolute; left: 34px; top: 92px; color: var(--white); }
  .person .name { font-size: 18px; font-weight: 700; }
  .person .role { font-size: 13px; margin-top: 4px; }

  .contact {
    position: absolute; left: 34px; top: 212px;
    color: var(--white); font-size: 13px; line-height: 1.35;
    list-style: none;
  }
  .contact li { display: flex; align-items: center; gap: 7px; }
  .contact .address { padding-left: 0; }
  .contact svg { width: 11px; height: 11px; flex: none; }
</style>
</head>
<body>
<main class="canvas">

  <section class="card card-back" aria-label="Business card back">
    <div class="brand-name"><span class="word-main">VELORA</span><span class="word-sub">TRAVEL</span></div>
    <div class="web">www.veloratravel.com</div>
  </section>

  <section class="card card-front" aria-label="Business card front">
    <svg class="shape" viewBox="0 0 560 320" aria-hidden="true">
      <circle cx="432" cy="128" r="238" fill="var(--ring-grey)"/>
      <circle cx="448" cy="116" r="232" fill="var(--white)"/>
    </svg>

    <div class="brand-name"><span class="word-main">VELORA</span><span class="word-sub">TRAVEL</span></div>

    <div class="person">
      <div class="name">Laura Bennett</div>
      <div class="role">Principal</div>
    </div>

    <ul class="contact">
      <li class="address">48 Harbour Lane, Westbrook</li>
      <li class="address">QC H2X 4K7</li>
      <li>
        <svg viewBox="0 0 12 12"><path fill="#fff" d="M1 4c0-2 2-3 5-3s5 1 5 3v1H8V4H4v1H1zM2 6h8l1 5H1z"/></svg>
        514.555.0187
      </li>
      <li>
        <svg viewBox="0 0 12 12"><rect x="0.5" y="2" width="11" height="8" fill="#fff"/><path d="M0.5 2l5.5 4.5L11.5 2" fill="none" stroke="var(--navy)" stroke-width="1"/></svg>
        lbennett@veloratravel.com
      </li>
      <li>
        <svg viewBox="0 0 12 12"><circle cx="6" cy="6" r="5.5" fill="#fff"/><path d="M4 4l4 2-4 2z" fill="var(--navy)"/></svg>
        www.veloratravel.com
      </li>
    </ul>
  </section>

</main>
</body>
</html>
```